Packaging design for high end, natural skin care line needed

Marisol Thackery Beauty needs a label design. It is a new skin care line I am launching.
For years my line Velvet Orchard Beauty was quite popular and featured in several magazines, but for personal reasons had to be shut down. Now I am launching a new line featuring VOB's top selling products, but focused solely on skin care more so than cosmetics. All products will still be handmade, but the line should still look professional-something worthy of a Brindle Market shelf!
I am branding it with my name, as I am often quoted in articles related to gluten in beauty products, so Marisol Thackery and beauty are key words.
The key products will be facial and body serums which are packaged in .5oz., 1oz. and larger amber glass bottles with black dropper tops, I will include pictures below. For dimensions, the labels can be any size that you think will work best, but need to at the least fit the 1oz. bottle, dimensions shown here http://www.corvelflask.example/amber-glass-tall-round-flask/p/QZ7K-93/
I loved the former VOB logo, but for Marisol Thackery Beauty I am looking for something more personal, more apothecary-like, and probably less colorful.
The line will be small, just a handful of products, but luxe, rich.
I am attaching photos of Velvet Orchard Beauty's packaging for your reference.
Thanks much!!

Hi Everyone! Thank you for your submissions! Please see the links I provided in the brief, I really am looking for something more technical looking, like an apothecary. And want black text on a white background, not a black background, and nothing flowery.
Thank you all!!
Marisol

Target Market(s)

My clients are primarily women of all ages, but with more of a skin care focus, and no longer a cosmetic one, I would also like to appeal to a male audience. My clients are health conscious, gluten-free, natural, paleo, or vegan, etc. Target age is probably 25-55. Products are a bit high end, priced $45-65.

Industry/Entity Type

Cosmetics

Requirements
Must have
• It must at least say Marisol Thackery, or can say Marisol Thackery Beauty, but "Beauty" is not necessary. And capitalization is open, try whatever you think serves the brand. Likely slogans or taglines that can be included but are not essential: Care for your skin. Love and care for your skin. Handmade with love in the USA. Handmade in the USA. Think modern day apothecary. Small batch scotch. Something fine, but custom, handmade.
Nice to have
• I like the aesthetic of Oribel Skin Care a bit http://www.oribelhollis.example.au/
And of Dorian Valtz as shown here http://www.pinboardia.example/pin/847302915563017442/
Also of something like this that is even customizable http://www.pinboardia.example/pin/58274106392285514/
Every product is handmade in small batches, with fine ingredients, a moderate price point of around $45-$65. And I will likely begin making custom orders. So there could be a space to say when it was made, or for whom. I would like to keep the colors classic though, I probably want to stay away from the bright pink on this one.
Should not have
• As I mentioned, probably want to stay away from a lot of color. I like black vs. gray for the text, as it will show up better in editorials. I must look good, but also photograph well. Thanks!

```html
<!DOCTYPE html>
<html lang="en">
<head>
<meta charset="utf-8">
<title>Marisol Thackery – Body Serum Label</title>
<link rel="stylesheet" href="https://fonts.googleapis.com/css2?family=Barlow+Semi+Condensed:wght@200;400;500&family=Courier+Prime:wght@400;700&display=swap">
<style>
  :root {
    --ink: #0c0c0c;
    --rule: #6a6a6a;
    --paper: #ffffff;
  }
  * { margin: 0; padding: 0; box-sizing: border-box; }
  html, body {
    width: 1000px;
    height: 1200px;
    overflow: hidden;
    background: var(--paper);
  }
  .label {
    position: relative;
    width: 1000px;
    height: 1200px;
    background: var(--paper);
    color: var(--ink);
    font-family: "Barlow Semi Condensed", "Arial Narrow", sans-serif;
  }
  .brand {
    position: absolute;
    top: 84px;
    left: 0;
    width: 1000px;
    text-align: center;
    font-size: 84px;
    font-weight: 400;
    line-height: 1;
    letter-spacing: 1px;
    white-space: nowrap;
  }
  .header-rule {
    position: absolute;
    top: 185px;
    left: 0;
    width: 1000px;
    height: 3px;
    background: var(--rule);
  }
  .marker {
    position: absolute;
    top: 302px;
    left: 484px;
    width: 43px;
    height: 43px;
    background: var(--ink);
  }
  .product {
    position: absolute;
    left: 0;
    width: 1000px;
    text-align: center;
    line-height: 1;
    white-space: nowrap;
  }
  .product__kind { top: 441px; font-size: 125px; font-weight: 200; letter-spacing: -2px; }
  .product__type { top: 563px; font-size: 127px; font-weight: 500; letter-spacing: -1px; }
  .footnote {
    position: absolute;
    font-family: "Courier Prime", "Courier New", monospace;
    line-height: 1;
    white-space: nowrap;
  }
  .footnote--origin { top: 1122px; left: 236px; font-size: 26px; font-weight: 700; letter-spacing: 2px; }
  .footnote--volume { top: 1104px; left: 612px; font-size: 46px; font-weight: 400; letter-spacing: 0; }
</style>
</head>
<body>
  <main class="label">
    <header>
      <h1 class="brand">MARISOL THACKERY</h1>
      <div class="header-rule"></div>
    </header>
    <div class="marker"></div>
    <h2 class="product product__kind">BODY</h2>
    <h2 class="product product__type">SERUM</h2>
    <p class="footnote footnote--origin">HANDMADE IN USA</p>
    <p class="footnote footnote--volume">1 ounce</p>
  </main>
</body>
</html>
```